Awesome ecommerce store banner needed!

We need a sharp, clear, strong banner for one of our subcategory pages on http://www.brivelloop.example
We'd like to incorporate the following image. We'd like the background to be gray or black. We are replacing the Wireless Intercoms banner that is orange (we hate it).
WE do like our other banners, however, so please use them as reference:
SIze: 980 x 380
Two raw images of the intercom we'd like you to encorporate have been included. Choose one or the other depending on what you think would be best. If using the single angle, please duplicate it. We want two intercoms in the banner
Simple and Clean is key:
Text: Wireless Intercoms
Text Color: Can be white/off gray
Text Style: Please keep it clean in line with the website
Background: Black/gray/white

```html
<!DOCTYPE html>
<html lang="en">
<head>
<meta charset="utf-8">
<title>Wireless Intercoms</title>
<link rel="stylesheet" href="https://fonts.googleapis.com/css2?family=Alfa+Slab+One&display=swap">
<style>
  :root {
    --bg-deep: #141414;
    --bg-mid: #2b2b2b;
    --bg-light: #3a3a3a;
    --title-ink: #0b0b0b;
    --title-glow: #ffffff;
    --device-silver: #b9b9b9;
    --device-dark: #1c1c1c;
  }
  html, body {
    margin: 0;
    padding: 0;
    width: 1200px;
    height: 465px;
    overflow: hidden;
    background: var(--bg-deep);
  }
  .banner {
    position: relative;
    width: 1200px;
    height: 465px;
    overflow: hidden;
    background: radial-gradient(ellipse at 40% 45%, var(--bg-light) 0%, var(--bg-mid) 45%, var(--bg-deep) 100%);
  }
  .banner__title {
    position: absolute;
    left: 37px;
    top: 118px;
    margin: 0;
    font-family: "Alfa Slab One", "Rockwell", serif;
    font-weight: 400;
    font-size: 86px;
    line-height: 107px;
    letter-spacing: 1px;
    color: var(--title-ink);
    text-transform: uppercase;
    text-shadow:
      0 0 4px var(--title-glow),
      0 0 10px var(--title-glow),
      0 0 18px rgba(255, 255, 255, 0.7);
  }
  .banner__title span { display: block; }
  .product {
    position: absolute;
    border-radius: 10px;
    background: linear-gradient(100deg, var(--device-silver) 0%, #d6d6d6 45%, #8a8a8a 62%, var(--device-dark) 66%, var(--device-dark) 100%);
  }
  .product--back {
    left: 692px;
    top: 24px;
    width: 300px;
    height: 276px;
  }
  .product--front {
    left: 857px;
    top: 104px;
    width: 306px;
    height: 318px;
  }
</style>
</head>
<body>
  <main class="banner">
    <h1 class="banner__title"><span>Wireless</span><span>Intercoms</span></h1>
    <div class="product product--back" role="img" aria-label="Silver and black wireless intercom unit with antenna, rear of pair"></div>
    <div class="product product--front" role="img" aria-label="Silver and black wireless intercom unit with antenna, front of pair"></div>
  </main>
</body>
</html>
```